Business card design for modern law firm

We need new business cards. Information about our law firm can be found at www.qrtl-recht.de. The business cards should include the information that we have offices in Berlin and Stuttgart. They should be customizable for all attorneys who are partially located in Berlin and partially in Stuttgart. Example of the information:
Jonas Ackermann
lawyer
Specialist lawyer for copyright and media law
Lindenweg 17, 70374 Stuttgart
ackermann@qrtl-recht.de
+49 711 483 15 260
www.qrtl-recht.de
It is important for us that we can edit the cards independently, i.e. exchange names and contact details.
In addition, a QR code for a VCard should be placed on the card.
The design of the old maps is attached; the new design should clearly distinguish itself from them. They should be more modern. The design is ideally based on the design of the website www.qrtl-recht.de.
Industry/Entity Type
Rechtsanwalt
Contact Information for Business Card
Siehe projektbeschreibung

```html
<!DOCTYPE html>
<html lang="de">
<head>
<meta charset="utf-8">
<title>QRTL Rechtsanwälte – Visitenkarte</title>
<link rel="stylesheet" href="https://fonts.googleapis.com/css2?family=Manrope:wght@400;500;700&display=swap">
<style>
  :root {
    --brand-green: #a6ce39;
    --ink-grey: #6d6e71;
    --paper: #ffffff;
    --backdrop: #e4e4e4;
    --back-mark: #7e7f82;
  }
  * { margin: 0; padding: 0; box-sizing: border-box; }
  html, body {
    width: 1200px;
    height: 1200px;
    overflow: hidden;
    background: var(--backdrop);
    font-family: "Manrope", sans-serif;
  }
  .card {
    position: absolute;
    left: 176px;
    width: 848px;
    height: 519px;
    overflow: hidden;
  }
  .card--front { top: 58px; background: var(--paper); }
  .card--back { top: 616px; background: var(--brand-green); }

  .front-shape {
    position: absolute;
    inset: 0;
    width: 100%;
    height: 100%;
  }
  .firm-name {
    position: absolute;
    display: flex;
    align-items: center;
    gap: 14px;
    font-weight: 700;
    letter-spacing: 0.02em;
    white-space: nowrap;
  }
  .firm-name__square {
    width: 24px;
    height: 24px;
    background: currentColor;
  }
  .card--front .firm-name {
    left: 65px;
    top: 74px;
    font-size: 36px;
    color: var(--brand-green);
  }

  .person {
    position: absolute;
    left: 65px;
    top: 210px;
  }
  .person__name {
    font-size: 38px;
    font-weight: 700;
    color: var(--brand-green);
    line-height: 1.2;
  }
  .person__role {
    font-size: 20px;
    font-weight: 400;
    color: var(--ink-grey);
    margin-top: 2px;
  }
  .person__specialty {
    font-size: 17px;
    font-weight: 500;
    color: var(--ink-grey);
    margin-top: 2px;
  }

  .contact-list {
    position: absolute;
    left: 65px;
    top: 332px;
    list-style: none;
  }
  .contact-list__item {
    display: flex;
    align-items: center;
    height: 33px;
    font-size: 21px;
    color: var(--ink-grey);
    white-space: nowrap;
  }
  .contact-list__icon {
    width: 16px;
    height: 16px;
    margin-right: 20px;
    fill: var(--brand-green);
    flex: none;
  }

  .back-brand {
    position: absolute;
    left: 0;
    right: 0;
    top: 205px;
    display: flex;
    flex-direction: column;
    align-items: center;
    gap: 14px;
  }
  .card--back .firm-name {
    position: static;
    font-size: 46px;
    color: var(--back-mark);
  }
  .offices {
    font-size: 20px;
    font-weight: 500;
    letter-spacing: 0.18em;
    text-transform: uppercase;
    color: var(--paper);
  }
  .vcard-code {
    position: absolute;
    right: 40px;
    bottom: 40px;
    width: 104px;
    height: 104px;
    background: var(--paper);
    border: 8px solid var(--paper);
    outline: 2px solid var(--back-mark);
    outline-offset: -10px;
  }
</style>
</head>
<body>

<section class="card card--front" aria-label="Vorderseite">
  <svg class="front-shape" viewBox="0 0 678 415" preserveAspectRatio="none" aria-hidden="true">
    <path fill="var(--brand-green)" d="M520,0 L678,0 L678,415 C640,335 540,280 410,255 C500,222 558,165 560,100 C562,55 548,22 520,0 Z"/>
  </svg>

  <div class="firm-name"><span class="firm-name__square"></span>QRTL Rechtsanwälte</div>

  <div class="person">
    <h1 class="person__name">Jonas Ackermann</h1>
    <p class="person__role">lawyer</p>
    <p class="person__specialty">Specialist lawyer for copyright and media law</p>
  </div>

  <ul class="contact-list">
    <li class="contact-list__item">
      <svg class="contact-list__icon" viewBox="0 0 16 16"><path d="M1 3h14v10H1z"/><path d="M1.5 3.5l6.5 4.8 6.5-4.8" fill="none" stroke="#fff" stroke-width="1.4"/></svg>
      ackermann@qrtl-recht.de
    </li>
    <li class="contact-list__item">
      <svg class="contact-list__icon" viewBox="0 0 16 16"><path d="M3.6 1.2l2.3 2.8-1.3 1.8c.9 2 2.5 3.7 4.6 4.7l1.8-1.3 2.8 2.3-1.4 2.3C6.8 13.6 2.4 9.2 1.3 2.6z"/></svg>
      +49 711 483 15 260
    </li>
    <li class="contact-list__item">
      <svg class="contact-list__icon" viewBox="0 0 16 16"><circle cx="8" cy="8" r="6.5" fill="none" stroke="var(--brand-green)" stroke-width="1.6"/><path d="M1.5 8h13M8 1.5c-3 3.5-3 9.5 0 13M8 1.5c3 3.5 3 9.5 0 13" fill="none" stroke="var(--brand-green)" stroke-width="1.3"/></svg>
      www.qrtl-recht.de
    </li>
    <li class="contact-list__item">
      <svg class="contact-list__icon" viewBox="0 0 16 16"><path d="M8 1a5 5 0 0 0-5 5c0 3.6 5 9 5 9s5-5.4 5-9a5 5 0 0 0-5-5zm0 7a2 2 0 1 1 0-4 2 2 0 0 1 0 4z"/></svg>
      Lindenweg 17, 70374 Stuttgart
    </li>
  </ul>
</section>

<section class="card card--back" aria-label="Rückseite">
  <div class="back-brand">
    <div class="firm-name"><span class="firm-name__square"></span>QRTL Rechtsanwälte</div>
    <p class="offices">Berlin · Stuttgart</p>
  </div>
  <div class="vcard-code" role="img" aria-label="vCard QR code"></div>
</section>

</body>
</html>
```